TRESSLY FACEBOOK DESIGN

I need new design for facebook https://www.facebook.com/tresslyitalia.
Our Businnes is Hair care , hair replacement , hair transplant . hair regrowth . i NEED MEDICAL AND PROFESSIONAL DESIGN. I NEED ALSO RESPONSIVE DESIGN

Target Market(s)

Consumers

Industry/Entity Type

MEDICAL AND COSMETICS

Colors
0054AA
0677BA
7BADD7
CADEEF
E8F1F8

Requirements
Must have
• MEDICAL
Nice to have
• RESPONSIVE DESIGN

```html
<!DOCTYPE html>
<html lang="it">
<head>
<meta charset="UTF-8">
<title>Tressly – Facebook Cover</title>
<link rel="stylesheet" href="https://fonts.googleapis.com/css2?family=Montserrat:wght@500;600;700&display=swap">
<style>
  :root {
    --navy: #0054AA;
    --blue: #0677BA;
    --sky: #2A9FD8;
    --mid: #7BADD7;
    --pale: #CADEEF;
    --mist: #E8F1F8;
    --white: #FFFFFF;
    --stage: #DCE6EE;
    --ink: #1F3B6E;
  }
  html, body {
    margin: 0;
    width: 1200px;
    height: 1200px;
    overflow: hidden;
    background: var(--stage);
    font-family: "Montserrat", sans-serif;
  }
  .cover {
    position: absolute;
    left: 118px;
    top: 346px;
    width: 965px;
    height: 507px;
    background: var(--white);
    overflow: hidden;
  }
  .cover__photo {
    position: absolute;
    left: 292px;
    top: 50px;
    width: 673px;
    height: 457px;
    background: linear-gradient(100deg, rgba(255,255,255,0) 0%, #e9edf1 18%, #c9cfd6 45%, #8f98a3 70%, #b9c1ca 100%);
  }
  .cover__ring {
    position: absolute;
    fill: none;
  }
  .cover__ring--top { left: 0; top: 0; }
  .cover__ring--bottom { right: 0; bottom: 0; }
  .brand {
    position: absolute;
    left: 54px;
    top: 104px;
  }
  .brand__row {
    display: flex;
    align-items: center;
    gap: 12px;
  }
  .brand__dot {
    width: 44px;
    height: 44px;
    border-radius: 50%;
    background: var(--mid);
  }
  .brand__name {
    font-weight: 600;
    font-size: 48px;
    line-height: 1;
    color: var(--navy);
    letter-spacing: -0.5px;
  }
  .brand__tagline {
    margin: 14px 0 0 3px;
    font-weight: 500;
    font-size: 12.2px;
    color: var(--navy);
    letter-spacing: 0.1px;
  }
  .headline {
    position: absolute;
    left: 50px;
    top: 257px;
    margin: 0;
    font-weight: 700;
    font-size: 49px;
    line-height: 50px;
    color: var(--sky);
    letter-spacing: -0.5px;
  }
  .body-copy {
    position: absolute;
    left: 50px;
    top: 416px;
    width: 368px;
    margin: 0;
    font-weight: 600;
    font-size: 11.5px;
    line-height: 19px;
    color: var(--ink);
  }
  .cover__wave {
    position: absolute;
    left: 0;
    bottom: 0;
  }
</style>
</head>
<body>
  <section class="cover" aria-label="Copertina Facebook Tressly">
    <div class="cover__photo" role="img" aria-label="Foto di una giovane coppia sorridente con capelli folti e scuri"></div>

    <svg class="cover__wave" width="965" height="60" viewBox="0 0 965 60" aria-hidden="true">
      <path d="M0 20 C 180 30, 300 8, 480 12 S 800 24, 965 14 L965 60 L0 60 Z" fill="var(--pale)" opacity="0.85"/>
    </svg>

    <svg class="cover__ring cover__ring--top" width="120" height="90" viewBox="0 0 120 90" aria-hidden="true">
      <circle cx="18" cy="-18" r="86" stroke="var(--blue)" stroke-width="36" fill="none"/>
    </svg>

    <svg class="cover__ring cover__ring--bottom" width="175" height="195" viewBox="0 0 175 195" aria-hidden="true">
      <circle cx="105" cy="122" r="82" stroke="var(--blue)" stroke-width="46" fill="none"/>
    </svg>

    <div class="brand">
      <div class="brand__row">
        <span class="brand__dot" aria-hidden="true"></span>
        <span class="brand__name">Tressly</span>
      </div>
      <p class="brand__tagline">CURA E REINTEGRAZIONE DEI CAPELLI</p>
    </div>

    <h1 class="headline">Ci prendiamo<br>cura dei tuoi<br>capelli</h1>
    <p class="body-copy">Lorem ipsum dolor sit amet, consectetur adipiscing elit, sed do eiusmod tempor.</p>
  </section>
</body>
</html>
```